Health Care Service Company Flyer

Company name: Bright Harbor Clinic
Slogan: Find out what you're made of
Website: brightharborclinic.ca

I need the flyer to contain the company name (will provide logo source file ASAP), the slogan in large font and a "find out more at harborclinic.ca"

Other important data to include in the flyer is:
Four bullet points with the following information:
*Track performance and fitness results over time
*Develop proprietary exercise and dietary programs based on actionable data
*Track muscle atrophy from injury, as well as muscle gain during rehabilitation
*Reveal imbalances in muscle symmetry and strength, flexibility, and joint mechanics

I also need the following information conveyed somewhere on the flyer:
*Body Fat, Muscle Mass, and Bone Density Measurements
• Over 50 data points generated in each 10 minute scan
*Call XXX-XXX-XXX to book an appointment today

DEXA Body Composition Services.
Get scanned today.

See example of competitor flyers in the images to get an example of the images and information we are trying to convey

Target Market(s)

athletes, fitness enthusiast, crossfit

Industry/Entity Type

Health And Wellness

Colors
33a6d7
acd036

Requirements
Nice to have
• Prefer images be general health and wellness related - in other words, individuals who look healthy, but are not abnormally muscular
Should not have
• Shirtless models, No big muscles,

```html
<!DOCTYPE html>
<html lang="en">
<head>
<meta charset="utf-8">
<title>Bright Harbor Clinic – DEXA Body Composition Flyer</title>
<link href="https://fonts.googleapis.com/css2?family=Roboto:ital,wght@0,300;0,400;0,500;0,700;1,500&family=Roboto+Condensed:wght@400;700&display=swap" rel="stylesheet">
<style>
  :root {
    --lime: #acd036;
    --charcoal: #3a3a3c;
    --ink: #2b2b2b;
    --page: #e9eaeb;
    --white: #ffffff;
    --band: rgba(150, 152, 155, 0.72);
  }
  * { box-sizing: border-box; margin: 0; padding: 0; }
  html, body { width: 854px; height: 1200px; overflow: hidden; }
  body { background: var(--page); font-family: "Roboto", Arial, sans-serif; position: relative; }

  .flyer {
    position: absolute; left: 57px; top: 68px; width: 745px; height: 1054px;
    background: var(--white); overflow: hidden;
    box-shadow: 0 2px 6px rgba(0,0,0,0.18);
  }
  .top-bar { position: absolute; left: 0; top: 0; width: 100%; height: 29px; background: var(--lime); }

  .hero-photo {
    position: absolute; left: 0; top: 29px; width: 100%; height: 423px;
    background: linear-gradient(160deg, #7fb6d3 0%, #cfe0ea 35%, #9aa3ad 65%, #e6e8ea 100%);
  }
  .title-band {
    position: absolute; left: 0; top: 264px; width: 100%; height: 104px;
    background: var(--band);
  }
  .title-rule { position: absolute; left: 177px; width: 382px; height: 2px; background: var(--lime); }
  .title-rule.upper { top: 14px; }
  .title-rule.lower { top: 88px; }
  .clinic-name {
    position: absolute; left: 0; top: 18px; width: 100%; text-align: center;
    font-style: italic; font-weight: 500; font-size: 50px; color: var(--white); line-height: 66px;
  }

  .slogan-bar {
    position: absolute; left: 0; top: 452px; width: 100%; height: 48px;
    background: var(--lime); color: var(--white);
    font-family: "Roboto Condensed", Arial, sans-serif; font-weight: 700; font-size: 25px;
    display: flex; align-items: center; justify-content: center; letter-spacing: 0.2px;
  }

  .benefits { position: absolute; left: 0; top: 500px; width: 100%; height: 182px; display: flex; }
  .benefit {
    flex: 1; position: relative; display: flex; flex-direction: column; align-items: center;
    padding-top: 24px; color: var(--white); text-align: center;
  }
  .benefit.gym { background: linear-gradient(180deg, #8a8f95, #4e5359); }
  .benefit.rehab { background: linear-gradient(180deg, #6d5f5a, #8b6f66); }
  .benefit.road { background: linear-gradient(180deg, #4b5157, #2f3337); }
  .benefit.joint { background: linear-gradient(180deg, #6a4e45, #8a6a5d); }
  .benefit + .benefit { border-left: 1px solid rgba(255,255,255,0.25); }
  .benefit-icon { width: 60px; height: 60px; }
  .benefit-text {
    margin-top: 14px; font-size: 12px; line-height: 15px; text-transform: uppercase;
    font-weight: 400; padding: 0 10px;
  }

  .services-heading {
    position: absolute; left: 33px; top: 690px;
    font-weight: 700; font-size: 37px; line-height: 44px; color: var(--lime); letter-spacing: 0.2px;
    white-space: nowrap;
  }
  .services-sub {
    position: absolute; left: 33px; top: 737px;
    font-weight: 300; font-size: 36px; line-height: 44px; color: var(--ink);
    white-space: nowrap;
  }

  .scan-box {
    position: absolute; left: 0; top: 795px; width: 443px; height: 87px;
    background: var(--charcoal); color: var(--white); padding: 10px 0 0 33px;
  }
  .scan-box .lead { font-weight: 500; font-size: 21px; line-height: 28px; }
  .scan-box .emphasis { font-weight: 500; font-size: 30px; line-height: 38px; }

  .measures { position: absolute; left: 33px; top: 898px; }
  .measures .lead { font-weight: 500; font-size: 21px; color: var(--ink); line-height: 30px; }
  .measures .emphasis { font-weight: 700; font-size: 29px; color: var(--lime); line-height: 38px; }

  .pointer { position: absolute; left: 347px; top: 958px; width: 56px; height: 39px; }

  .partner {
    position: absolute; left: 470px; top: 918px; display: flex; align-items: center; gap: 16px;
  }
  .partner-dot { width: 44px; height: 44px; border-radius: 50%; background: var(--ink); }
  .partner-name { font-weight: 700; font-size: 22px; line-height: 28px; color: var(--ink); letter-spacing: 1.5px; }

  .contact-bar {
    position: absolute; left: 0; top: 996px; width: 100%; height: 58px;
    background: var(--lime); color: var(--white); font-size: 18px; font-weight: 300;
    display: flex; align-items: center; justify-content: center; gap: 14px;
  }
  .contact-bar strong { font-weight: 700; }
  .contact-sep { width: 9px; height: 9px; border-radius: 50%; background: var(--white); }
</style>
</head>
<body>
<div class="flyer">
  <div class="top-bar"></div>

  <div class="hero-photo" role="img" aria-label="Photo of a smiling couple shaking hands with a doctor in a bright clinic lobby"></div>
  <div class="title-band">
    <div class="title-rule upper"></div>
    <h1 class="clinic-name">Bright Harbor Clinic</h1>
    <div class="title-rule lower"></div>
  </div>

  <div class="slogan-bar">FIND OUT WHAT YOU'RE MADE OF</div>

  <div class="benefits">
    <div class="benefit gym" role="img" aria-label="Photo of a woman training in a gym">
      <svg class="benefit-icon" viewBox="0 0 64 64" fill="none" stroke="#fff" stroke-width="4" stroke-linecap="round" stroke-linejoin="round">
        <circle cx="34" cy="36" r="20"/><path d="M34 24v12l8 6"/><path d="M28 10h12M34 10v6"/>
      </svg>
      <p class="benefit-text">Track performance<br>and fitness results<br>over time</p>
    </div>
    <div class="benefit rehab" role="img" aria-label="Photo of a back with muscle pain during rehabilitation">
      <svg class="benefit-icon" viewBox="0 0 64 64" fill="none" stroke="#fff" stroke-width="4" stroke-linejoin="round">
        <rect x="8" y="8" width="48" height="48" rx="4"/><path d="M32 18v28M18 32h28"/>
      </svg>
      <p class="benefit-text">Track muscle atrophy<br>from injury, as well<br>as muscle gain during<br>rehabilitation</p>
    </div>
    <div class="benefit road" role="img" aria-label="Photo of a runner on an open road">
      <svg class="benefit-icon" viewBox="0 0 64 64" fill="none" stroke="#fff" stroke-width="4" stroke-linecap="round" stroke-linejoin="round">
        <path d="M8 56h48"/><path d="M14 56V40M26 56V30M38 56V36M50 56V18"/><path d="M12 30l14-12 12 8 16-16"/>
      </svg>
      <p class="benefit-text">Develop proprietary<br>exercise and dietary<br>programs based on<br>actionable data</p>
    </div>
    <div class="benefit joint" role="img" aria-label="Photo of a person holding a sore shoulder">
      <svg class="benefit-icon" viewBox="0 0 64 64" fill="none" stroke="#fff" stroke-width="3.5" stroke-linecap="round" stroke-linejoin="round">
        <path d="M32 8v44M12 16h40M22 56h20"/><path d="M12 16l-8 18h16z"/><path d="M52 16l-8 18h16z"/>
      </svg>
      <p class="benefit-text">Reveal imbalances<br>in muscle symmetry<br>and strength,<br>flexibility, and joint<br>mechanics</p>
    </div>
  </div>

  <h2 class="services-heading">DEXA Body Composition Services.</h2>
  <p class="services-sub">Get scanned today.</p>

  <div class="scan-box">
    <p class="lead">Over 50 data points generated in each</p>
    <p class="emphasis">10 minute scan</p>
  </div>

  <div class="measures">
    <p class="lead">Body Fat, Muscle Mass, and Bone</p>
    <p class="emphasis">Density Measurements</p>
  </div>

  <svg class="pointer" viewBox="0 0 56 39"><polygon points="28,0 56,39 0,39" fill="#acd036"/></svg>

  <div class="partner">
    <span class="partner-dot"></span>
    <span class="partner-name">NORTHWIND VET</span>
  </div>

  <div class="contact-bar">
    <span><strong>Call:</strong> XXX-XXX-XXX to book an appointment today</span>
    <span class="contact-sep"></span>
    <span><strong>Email:</strong> brightharborclinic.ca</span>
  </div>
</div>
</body>
</html>
```